Keep Tomorrow Book Cover

I am looking for book front cover ideas. The book trim size will be 5.5 x 8.5 in so please make the mock up that size. The book Title is "Keep Tomorrow" and the Subtitle is "Counsel for the Crossroads Nobody Warns You About". The audience for the book is leaders in high-growth companies. It consists of a series of letters and advice for specific problems the leader will encounter on their journey. The design needs to be attractive to both male and female readers. I am attaching a file with brand colors and some rough ideas that need to be refined. The examples lean toward a feminine vibe but I want the cover to be more universal. Please use the brand colors identified in the file.

```html
<!DOCTYPE html>
<html lang="en">
<head>
<meta charset="utf-8">
<title>Keep Tomorrow – Book Cover</title>
<link href="https://fonts.googleapis.com/css2?family=Ubuntu:wght@700&family=Caveat+Brush&family=Roboto:wght@700&display=swap" rel="stylesheet">
<style>
  :root {
    --paper: #f7f4ef;
    --terracotta: #b07a5e;
    --forest: #3e5a4e;
    --sage: #7f9a84;
    --slate-blue: #879cb0;
    --kraft: #e8bf9c;
    --foliage: #6f8a78;
    --white: #f8f6f2;
  }
  html, body {
    margin: 0;
    padding: 0;
    overflow: hidden;
    background: var(--paper);
  }
  .cover {
    position: relative;
    width: 776px;
    height: 1200px;
    background: var(--paper);
    overflow: hidden;
  }
  .cover-art {
    position: absolute;
    left: 136px;
    top: 300px;
    width: 504px;
    height: 548px;
    border-radius: 40% 40% 6px 6px;
    background:
      radial-gradient(ellipse at 50% 38%, var(--foliage) 0%, rgba(111,138,120,0.55) 45%, rgba(111,138,120,0) 72%),
      linear-gradient(to bottom, rgba(232,191,156,0) 0%, rgba(232,191,156,0) 52%, var(--kraft) 53%, #dcae88 100%);
    z-index: 1;
  }
  .title {
    position: absolute;
    top: 62px;
    left: 0;
    width: 100%;
    margin: 0;
    text-align: center;
    font-family: "Ubuntu", sans-serif;
    font-weight: 700;
    color: var(--terracotta);
    font-size: 136px;
    line-height: 150px;
    letter-spacing: -2px;
    text-shadow: 0 0 14px var(--white), 0 0 6px var(--white);
    z-index: 2;
  }
  .title span { display: block; }
  .subtitle {
    position: absolute;
    top: 868px;
    left: 0;
    width: 100%;
    margin: 0;
    text-align: center;
    font-family: "Caveat Brush", cursive;
    font-weight: 400;
    color: var(--forest);
    font-size: 46px;
    line-height: 60px;
  }
  .subtitle span { display: block; }
  .divider {
    position: absolute;
    left: 320px;
    top: 1036px;
  }
  .author-band {
    position: absolute;
    left: 0;
    bottom: 0;
    width: 776px;
    height: 112px;
  }
  .author {
    position: absolute;
    left: 0;
    width: 100%;
    top: 1118px;
    margin: 0;
    text-align: center;
    font-family: "Roboto", sans-serif;
    font-weight: 700;
    font-size: 34px;
    color: var(--white);
    letter-spacing: 0.2px;
  }
</style>
</head>
<body>
  <main class="cover">
    <h1 class="title"><span>Keep</span><span>Tomorrow</span></h1>

    <div class="cover-art" role="img" aria-label="Watercolour illustration of an open kraft envelope overflowing with eucalyptus leaves, white daisies and coral wildflowers"></div>

    <p class="subtitle"><span>Counsel for the Crossroads</span><span>Nobody Warns You About</span></p>

    <svg class="divider" width="136" height="16" viewBox="0 0 136 16" aria-hidden="true">
      <line x1="4" y1="8" x2="134" y2="7" stroke="var(--sage)" stroke-width="3" stroke-linecap="round"/>
    </svg>

    <svg class="author-band" viewBox="0 0 776 112" preserveAspectRatio="none" aria-hidden="true">
      <path fill="var(--slate-blue)" d="M0 14 L30 12 L62 15 L95 10 L130 13 L170 9 L205 12 L240 6 L262 9 L300 5 L340 10 L380 7 L420 11 L455 8 L490 12 L520 9 L560 13 L600 9 L640 12 L680 8 L720 12 L750 9 L776 11 L776 112 L0 112 Z"/>
    </svg>
    <p class="author">Naomi Achieng Ward</p>
  </main>
</body>
</html>
```